Veltaro Clear Springs needs a new business card design (we produce and sell pure bottled water)

We need a clean modern design for our new business cards, We have an existing logo which ultimately cannot be changed, however it could be slighty improved and the colours adjusted. We have this existing logo on all of our bottles, vehicles etc.

Our company slogan is "Pure down to the last drop".
Along with our relevant company information
(Address, phone, website email etc) we will only be using names and not putting position titles for flexibilty.

We are looking for a clean, minimalist modern design.

You can view our website (if need of an update also!) to see our business.

Contact Information for Business Card

Staff Name : XXXXXX XXXXXX
Address : 8/41 Dunmore St
Halden Flats QLD 4261
Staff Mobile Number : 04XX XXX XXX
Office Phone Number : 07 3915 2047
Staff Email Address : XXXX@veltaroclearsprings.com.au
Website : www.veltaroclearsprings.com.au

Font styles to use
Sans Serif

Colors
cee9f5
33a6d7
0492cd
0455a3
3276b5
85abd2
cedeed

Requirements
Must have
• The ability to edit and change the staff members details as we will need to edit for each respective staff member (7 in total)

```html
<!DOCTYPE html>
<html lang="en">
<head>
<meta charset="utf-8">
<title>Veltaro Clear Springs – Business Card</title>
<link rel="stylesheet" href="https://fonts.googleapis.com/css2?family=Arimo:wght@700&display=swap">
<style>
  :root {
    --page: #eef1f4;
    --front-bg: #cee9f5;
    --back-bg: #ffffff;
    --navy: #1f2a8c;
    --text-blue: #0455a3;
    --water-light: #cedeed;
    --water-mid: #85abd2;
  }
  * { box-sizing: border-box; margin: 0; padding: 0; }
  html, body { width: 975px; height: 1200px; overflow: hidden; }
  body {
    background: var(--page);
    font-family: "Arimo", Arial, sans-serif;
    font-weight: 700;
    position: relative;
  }
  .card {
    position: absolute;
    left: 88px;
    width: 800px;
    height: 470px;
    overflow: hidden;
    box-shadow: 0 4px 18px rgba(20, 40, 80, 0.15);
  }
  .card--front { top: 90px; background: var(--front-bg); }
  .card--back { top: 640px; background: var(--back-bg); }

  .brand {
    display: flex;
    align-items: center;
    gap: 14px;
    color: var(--navy);
  }
  .brand__dot {
    width: 30px; height: 30px;
    border-radius: 50%;
    background: var(--navy);
    flex: none;
  }
  .card--front .brand {
    position: absolute;
    inset: 0;
    justify-content: center;
    font-size: 40px;
  }
  .card--back .brand {
    position: absolute;
    right: 44px; top: 68px;
    font-size: 21px;
    gap: 10px;
  }
  .card--back .brand__dot { width: 18px; height: 18px; }

  .water-art {
    position: absolute;
    inset: 0;
    background:
      radial-gradient(ellipse 62% 58% at 58% 44%, #ffffff 0%, #ffffff 55%, rgba(255,255,255,0) 100%),
      linear-gradient(135deg, var(--water-light) 0%, var(--water-mid) 55%, var(--water-light) 100%);
  }
  .staff-name {
    position: absolute;
    left: 200px; top: 112px;
    font-size: 38px;
    letter-spacing: 1px;
    color: var(--text-blue);
  }
  .contact {
    position: absolute;
    left: 358px; top: 228px;
    list-style: none;
    color: var(--text-blue);
    font-size: 22px;
    line-height: 1.1;
  }
  .contact__item {
    display: flex;
    align-items: flex-start;
    gap: 14px;
    margin-bottom: 17px;
  }
  .contact__icon { width: 22px; height: 22px; flex: none; margin-top: 1px; }
  .contact__icon--solid { fill: var(--text-blue); }
  .contact__icon--line { fill: none; stroke: var(--text-blue); stroke-width: 1.6; }
</style>
</head>
<body>

<section class="card card--front" aria-label="Card front">
  <div class="brand"><span class="brand__dot"></span><span class="brand__name">Veltaro Clear Springs</span></div>
</section>

<section class="card card--back" aria-label="Card back">
  <div class="water-art" role="img" aria-label="Photo of a curling splash of clear water framing the card"></div>

  <div class="brand"><span class="brand__dot"></span><span class="brand__name">Veltaro Clear Springs</span></div>

  <h1 class="staff-name">MAREK</h1>

  <ul class="contact">
    <li class="contact__item">
      <svg class="contact__icon contact__icon--solid" viewBox="0 0 24 24"><path d="M7 2h10a2 2 0 0 1 2 2v16a2 2 0 0 1-2 2H7a2 2 0 0 1-2-2V4a2 2 0 0 1 2-2zm0 3v13h10V5z"/></svg>
      <span>07 3915 2047</span>
    </li>
    <li class="contact__item">
      <svg class="contact__icon contact__icon--solid" viewBox="0 0 24 24"><path d="M2 5h20v14H2zm2 2v.5l8 5.5 8-5.5V7zm0 3v7h16v-7l-8 5.5z"/></svg>
      <span>veltaroclearsprings@mailbox.com</span>
    </li>
    <li class="contact__item">
      <svg class="contact__icon contact__icon--line" viewBox="0 0 24 24"><circle cx="12" cy="12" r="9"/><ellipse cx="12" cy="12" rx="4" ry="9"/><path d="M3 12h18M5 7h14M5 17h14"/></svg>
      <span>www.veltaroclearsprings.com.au</span>
    </li>
    <li class="contact__item">
      <svg class="contact__icon contact__icon--solid" viewBox="0 0 24 24"><path d="M12 3l10 9h-3v9h-5v-6h-4v6H5v-9H2z"/></svg>
      <span>8/41 Dunmore St Halden<br>Flats QLD 4261</span>
    </li>
  </ul>
</section>

</body>
</html>
```